Business card for a Exhibition booth fabrication company

Hi. My company would like to change our corporate name card. We are an events and Exhibition stand builder company. We would like our corporate name card to resonate what we do. I need someone to create something unique that relates to the industry that I am in. The graphic designer should be creative to incorporate the elements of my industry and try to blend in well in the design of the card. Our aim is to ensure that we are unique and our card can look different from our competitors.
Updates

The decision maker was very busy and didnt had time to make this decision

Target Market(s)

Marketing and events manager from all companies

Contact Information for Business Card

The business card should have the following details:
Name
Job Title
Email
Website

Colors

Designer to choose colors to be used in the design.

Requirements
Must have
• The card must be look something that is relevant to the service that I am providing. My website is: www.velmora-buildworks.example
• You can see my website to get more information on what service that I am doing
Nice to have
• On the back of my card, I would like to have a globe image with the incorporation of my company logo. This is to indicate that my services can be done in any part of the world.

```html
<!DOCTYPE html>
<html lang="en">
<head>
<meta charset="utf-8">
<title>Velmora Buildworks – Business Card</title>
<link rel="stylesheet" href="https://fonts.googleapis.com/css2?family=Open+Sans:wght@400;600&family=Michroma&display=swap">
<style>
  :root {
    --backdrop: #d9d9db;
    --card: #1f2022;
    --card-edge: #2a2b2e;
    --red: #e3242b;
    --white: #f2f2f2;
    --grey: #b9b9bb;
    --rule: #5c5d60;
    --map-a: #3a3b3e;
    --map-b: #2a2b2e;
  }
  * { box-sizing: border-box; margin: 0; padding: 0; }
  html, body { width: 1200px; height: 1108px; overflow: hidden; }
  body {
    background: var(--backdrop);
    font-family: "Open Sans", sans-serif;
    display: flex;
    justify-content: center;
    align-items: center;
    gap: 80px;
  }
  .card {
    width: 420px;
    height: 680px;
    border-radius: 26px;
    background: var(--card);
    position: relative;
    overflow: hidden;
    box-shadow: 0 14px 34px rgba(0,0,0,0.25);
  }
  /* Front */
  .brand {
    position: absolute;
    top: 170px;
    left: 0; right: 0;
    display: flex;
    justify-content: center;
    align-items: center;
    gap: 12px;
  }
  .brand-dot {
    width: 14px; height: 14px; border-radius: 50%;
    background: var(--red);
  }
  .brand-name {
    font-family: "Michroma", sans-serif;
    font-size: 21px;
    letter-spacing: 2px;
    color: var(--grey);
    text-transform: uppercase;
  }
  .contact {
    position: absolute;
    right: 40px;
    left: 40px;
    bottom: 80px;
    text-align: right;
  }
  .person-name {
    font-family: "Michroma", sans-serif;
    font-size: 24px;
    color: var(--red);
    text-transform: uppercase;
    letter-spacing: 1px;
  }
  .person-title {
    font-size: 17px;
    color: var(--white);
    margin-top: 2px;
  }
  .divider {
    height: 1px;
    background: var(--rule);
    width: 220px;
    margin: 14px 0 12px auto;
  }
  .contact-line {
    font-size: 16px;
    line-height: 1.55;
    color: var(--white);
  }
  .label { color: var(--red); font-weight: 600; }
  .place { color: var(--red); }
  .website { font-size: 16px; color: var(--red); line-height: 1.55; }
  /* Back */
  .world-map {
    position: absolute;
    top: 30px; left: 20px; right: 20px;
    height: 370px;
    border-radius: 12px;
    background: radial-gradient(ellipse at 50% 45%, var(--map-a), var(--map-b) 75%);
  }
  .services {
    position: absolute;
    top: 410px; left: 0; right: 0;
    list-style: none;
    text-align: center;
  }
  .services li {
    font-size: 17px;
    line-height: 1.42;
    color: var(--white);
  }
</style>
</head>
<body>
  <section class="card card-front">
    <div class="brand">
      <span class="brand-dot"></span>
      <span class="brand-name">Velmora Buildworks</span>
    </div>
    <div class="contact">
      <div class="person-name">Daniel Hart</div>
      <div class="person-title">Managing Director</div>
      <div class="divider"></div>
      <div class="contact-line"><span class="label">P:</span> +65 81402736 <span class="place">(Singapore)</span></div>
      <div class="contact-line"><span class="label">P:</span> +974 55208419 <span class="place">(Qatar)</span></div>
      <div class="contact-line"><span class="label">E:</span> info@velmora-buildworks.example</div>
      <div class="website">www.velmora-buildworks.example</div>
    </div>
  </section>

  <section class="card card-back">
    <div class="world-map" role="img" aria-label="Dotted world map in dark grey"></div>
    <ul class="services">
      <li>Exhibition Booth Fabrication</li>
      <li>Outdoor Booth Setup</li>
      <li>Interior Design</li>
      <li>Installation and Dismantle</li>
      <li>Exhibition Management</li>
      <li>Shell Scheme Display Booth</li>
      <li>Custom Stand Design</li>
      <li>Exhibition Furniture and Equipment</li>
      <li>Exhibition Project Management</li>
    </ul>
  </section>
</body>
</html>
```